Oak Fitness postcard

*my business is a fitness business. I offer at home personal fitness training. I don't own a gym, I go house to house training people.
*I would like the flyer to have a colorful enviroment with a picture of a happy and fit woman, because women are my target market. Mabey have her excersing or being trained by a male fitness trainer.
*For the headline, I don't want the title of my business, instead I want an exciting headline. Something mabey like "fit in the the jeans you love" anything that says the client could lose weight
*for the services please add- training at your home. Meal plans based on foods you love. Educate you of proper dieting and nutrition. High protein dieting
*for benifits please add- reduce cellulite. Rdeuce stretch marks. Lose Permanente weight. Flatten and tone stomach. Sleep better.
*I am offering 1 full free training session with no obligation, please put that in big bold letters
*please make the before and after pic blend into the design and add the testimonial "Losing weight felt impossible till I went on a high protein diet, then the pounds dropped rapidly." Delia M from Boston MS.
*on top of the before and after pic, please add "proof that high protein diets work"
*in big bold letters at the bottom or center please add a call to action saying something like "CALL 734-518-3906 and ask about my free training session"
*at bottom of flyer my contact info is "derek Holloway (certified personal trainer and nutritional specialist)" and phone number "734-518-3906" business name "oak fitness"

Industry/Entity Type

Business

```html
<!DOCTYPE html>
<html lang="en">
<head>
<meta charset="utf-8">
<title>Oak Fitness – In-Home Training Postcard</title>
<link rel="stylesheet" href="https://fonts.googleapis.com/css2?family=Raleway:ital,wght@0,400;0,500;0,600;1,400&family=Montserrat:wght@700;800&family=Roboto+Condensed:wght@400;500;700&display=swap">
<style>
  :root {
    --brand-blue: #2a5eab;
    --brand-red: #e8392a;
    --accent-sky: #5cb3e8;
    --ink-white: #ffffff;
    --phone-tile: #1f62b8;
  }
  * { margin: 0; padding: 0; box-sizing: border-box; }
  html, body { width: 1200px; height: 930px; overflow: hidden; background: var(--brand-blue); }
  .postcard {
    position: relative;
    width: 1200px;
    height: 930px;
    background: var(--brand-blue);
    color: var(--ink-white);
    font-family: "Raleway", sans-serif;
    overflow: hidden;
  }
  .hero-art { position: absolute; left: 0; top: 0; width: 700px; height: 816px; }

  .headline {
    position: absolute; left: 563px; top: 20px;
    font-family: "Raleway", sans-serif; font-weight: 500;
    font-size: 48px; letter-spacing: -1.2px;
    color: var(--brand-red); white-space: nowrap;
  }
  .subhead {
    position: absolute; left: 657px; top: 78px;
    font-family: "Raleway", sans-serif; font-weight: 400;
    font-size: 34px; letter-spacing: -1.6px; white-space: nowrap;
  }
  .benefit-list {
    position: absolute; left: 658px; top: 136px; list-style: none;
    font-family: "Montserrat", sans-serif; font-weight: 700;
    font-size: 21.5px; letter-spacing: -0.6px; line-height: 28.7px;
  }
  .benefit-list li { position: relative; padding-left: 38px; }
  .benefit-list li::before {
    content: ""; position: absolute; left: 2px; top: 5px;
    width: 22px; height: 22px; border-radius: 50%;
    background: var(--brand-red);
  }
  .benefit-list li::after {
    content: ""; position: absolute; left: 8px; top: 12px;
    width: 6px; height: 6px;
    border-top: 2.5px solid var(--ink-white); border-right: 2.5px solid var(--ink-white);
    transform: rotate(45deg);
  }

  .offer-burst { position: absolute; left: 616px; top: 470px; width: 260px; height: 260px; }
  .offer-burst svg { position: absolute; inset: 0; }
  .offer-text {
    position: absolute; inset: 0; display: flex; flex-direction: column;
    align-items: center; justify-content: center; text-align: center;
    font-family: "Roboto Condensed", sans-serif; font-weight: 400;
    font-size: 30px; line-height: 29px; text-transform: uppercase;
  }
  .offer-text .big-one { font-weight: 700; font-size: 34px; }

  .proof-caption {
    position: absolute; left: 900px; top: 378px;
    font-size: 16px; letter-spacing: -0.6px; white-space: nowrap;
  }
  .results-frame {
    position: absolute; left: 888px; top: 408px; width: 270px; height: 282px;
    background: var(--brand-red); padding: 7px;
    display: flex; gap: 7px;
  }
  .result-photo { flex: 1; height: 100%; }
  .result-photo.before { background: linear-gradient(180deg, #a67a4f 0%, #d8c9c6 45%, #7d8fb2 100%); }
  .result-photo.after { background: linear-gradient(180deg, #ece7df 0%, #8f8a86 50%, #f2f1ee 100%); }

  .testimonial {
    position: absolute; left: 897px; top: 697px; width: 270px;
    font-style: italic; font-size: 16.5px; letter-spacing: -0.6px; line-height: 21.5px;
    white-space: nowrap;
  }
  .testimonial-author {
    position: absolute; right: 40px; top: 771px;
    font-size: 16.5px; letter-spacing: -0.5px; white-space: nowrap;
  }

  .contact-band {
    position: absolute; left: 0; top: 816px; width: 1200px; height: 114px;
    background: var(--brand-red); text-align: center;
  }
  .trainer-line {
    position: absolute; left: 0; right: 0; top: 7px;
    font-size: 29px; letter-spacing: -1.3px; white-space: nowrap;
  }
  .trainer-line .trainer-name { font-size: 34px; text-transform: uppercase; letter-spacing: -1.2px; }
  .phone-line {
    position: absolute; left: 331px; top: 52px;
    display: flex; align-items: center; gap: 13px; white-space: nowrap;
  }
  .phone-tile {
    width: 42px; height: 42px; border-radius: 6px; background: var(--phone-tile);
    display: flex; align-items: center; justify-content: center;
  }
  .phone-number { font-size: 46px; letter-spacing: -1.5px; line-height: 1; }
  .business-name { font-size: 30px; letter-spacing: -1.2px; }
</style>
</head>
<body>
<div class="postcard">

  <svg class="hero-art" viewBox="0 0 700 816">
    <defs>
      <linearGradient id="gymTone" x1="0" y1="0" x2="1" y2="0">
        <stop offset="0" stop-color="#7d8794"/>
        <stop offset="0.4" stop-color="#8d949c"/>
        <stop offset="0.6" stop-color="#c49a7e"/>
        <stop offset="1" stop-color="#3b4c6b"/>
      </linearGradient>
      <linearGradient id="gymShade" x1="0" y1="0" x2="0" y2="1">
        <stop offset="0" stop-color="#4a5562" stop-opacity="0.35"/>
        <stop offset="0.55" stop-color="#4a5562" stop-opacity="0"/>
        <stop offset="1" stop-color="#1e2533" stop-opacity="0.55"/>
      </linearGradient>
    </defs>
    <g role="img" aria-label="Photo of a smiling male trainer with a clipboard coaching a fit, happy woman in workout wear inside a gym">
      <path d="M0 0 H472 C590 140 650 300 632 420 C620 560 580 700 520 816 H0 Z" fill="url(#gymTone)"/>
      <path d="M0 0 H472 C590 140 650 300 632 420 C620 560 580 700 520 816 H0 Z" fill="url(#gymShade)"/>
    </g>
    <path d="M472 0 C590 140 650 300 632 420 C620 560 580 700 520 816" fill="none" stroke="var(--accent-sky)" stroke-width="8"/>
  </svg>

  <h1 class="headline">FIT IN THE JEANS YOU LOVE</h1>
  <p class="subhead">training at your home BENEFITS</p>

  <ul class="benefit-list">
    <li>Meal plans based on foods you love</li>
    <li>Educate you of proper dieting<br>and nutrition</li>
    <li>High protein dieting</li>
    <li>Reduce cellulite</li>
    <li>Reduce stretch marks</li>
    <li>Lose Permanente weight.</li>
    <li>Flatten and tone stomach</li>
    <li>Sleep better</li>
  </ul>

  <div class="offer-burst">
    <svg viewBox="0 0 260 260" aria-hidden="true">
      <polygon fill="var(--brand-red)" points="260,130 236.7,146.8 253.6,170.2 226.2,179 235.2,206.4 206.4,206.4 206.4,235.2 179,226.2 170.2,253.6 146.8,236.7 130,260 113.2,236.7 89.8,253.6 81,226.2 53.6,235.2 53.6,206.4 24.8,206.4 33.8,179 6.4,170.2 23.3,146.8 0,130 23.3,113.2 6.4,89.8 33.8,81 24.8,53.6 53.6,53.6 53.6,24.8 81,33.8 89.8,6.4 113.2,23.3 130,0 146.8,23.3 170.2,6.4 179,33.8 206.4,24.8 206.4,53.6 235.2,53.6 226.2,81 253.6,89.8 236.7,113.2"/>
    </svg>
    <div class="offer-text">
      <span><span class="big-one">1</span> Full free</span>
      <span>Training</span>
      <span>Session with</span>
      <span>No obligation</span>
    </div>
  </div>

  <p class="proof-caption">proof that high protein diets work</p>
  <div class="results-frame">
    <div class="result-photo before" role="img" aria-label="Before photo of the client standing in a pink plaid hoodie and jeans"></div>
    <div class="result-photo after" role="img" aria-label="After photo of the client taking a slimmer mirror selfie"></div>
  </div>

  <p class="testimonial">“Losing weight felt impossible till<br>I went on a high protein diet,<br>then the pounds dropped rapidly.”</p>
  <p class="testimonial-author">Delia M from Boston MS</p>

  <footer class="contact-band">
    <p class="trainer-line"><span class="trainer-name">Derek Holloway</span> - Certified personal trainer and nutritional specialist</p>
    <div class="phone-line">
      <span class="phone-tile">
        <svg width="26" height="30" viewBox="0 0 24 28" aria-hidden="true">
          <path fill="var(--brand-red)" d="M6 1 L10 2 L11 9 L8 11 C8 15 10 19 13 21 L16 19 L21 22 L20 27 C10 27 3 17 3 7 C3 4 4 2 6 1 Z"/>
        </svg>
      </span>
      <span class="phone-number">734-518-3906</span>
      <span class="business-name">- oak fitness</span>
    </div>
  </footer>

</div>
</body>
</html>
```